Redesign of an insurance website

Attached is an insurance website that I need to redesign. Currently the website is too dark. I like for example www.brenvalo.com . Could you make the website lighter and change the structure a little so that it is more user friendly?

Industry/Entity Type

Insurance

Number of Pages Required

4 page

```html
<!DOCTYPE html>
<html lang="cs">
<head>
<meta charset="utf-8">
<title>Jistotka.cz</title>
<link rel="stylesheet" href="https://fonts.googleapis.com/css2?family=Noto+Serif:wght@700&family=Open+Sans:wght@400;600&family=Lato:wght@700&display=swap">
<style>
  :root {
    --blue: #2a84ff;
    --orange: #f4621c;
    --dark: #3a3a3a;
    --ink: #1e1e1e;
    --muted: #6b6b6b;
    --line: #c9c9c9;
    --band: #f1f1f1;
    --white: #ffffff;
    --arrow: #a9a9a9;
  }
  * { box-sizing: border-box; margin: 0; padding: 0; }
  html, body { width: 1200px; height: 815px; overflow: hidden; background: var(--white); }
  body { position: relative; font-family: "Open Sans", sans-serif; color: var(--muted); }

  .site-header { position: absolute; left: 0; top: 0; width: 1200px; height: 94px; background: var(--blue); }
  .brand { position: absolute; left: 98px; top: 29px; font-family: "Noto Serif", serif; font-weight: 700; font-size: 29px; color: var(--white); letter-spacing: 0.3px; }
  .main-nav { position: absolute; left: 512px; top: 30px; display: flex; align-items: center; height: 34px; font-family: "Lato", sans-serif; font-weight: 700; font-size: 15.5px; color: var(--white); }
  .main-nav .nav-link { margin-right: 36px; }
  .nav-button { height: 34px; padding: 0 15px; display: flex; align-items: center; border: 1px solid var(--white); border-radius: 3px; margin-left: 16px; font-weight: 400; }
  .nav-button.login { background: var(--orange); margin-left: -8px; }
  .nav-button.register { background: var(--dark); }

  .intro-title { position: absolute; left: 0; top: 178px; width: 1200px; text-align: center; font-family: "Noto Serif", serif; font-weight: 700; font-size: 26px; color: var(--ink); }

  .product-carousel { position: absolute; left: 395px; top: 237px; }
  .product-label { position: absolute; left: 0; top: 381px; width: 1200px; text-align: center; font-family: "Noto Serif", serif; font-weight: 700; font-size: 14.5px; color: var(--ink); }

  .quote-form .field { position: absolute; top: 436px; width: 258px; height: 42px; border: 1px solid var(--line); border-radius: 2px; background: linear-gradient(#ffffff, #f2f2f2); padding-left: 19px; font-size: 13.5px; line-height: 40px; color: var(--muted); }
  .field.first-name { left: 199px; }
  .field.surname { left: 471px; }
  .field.email { left: 743px; }
  .consent { position: absolute; left: 491px; top: 503px; display: flex; align-items: center; font-size: 13.5px; }
  .consent .box { width: 10px; height: 10px; border: 1px solid #555; border-radius: 2px; margin-right: 13px; }
  .submit { position: absolute; left: 515px; top: 544px; width: 171px; height: 42px; background: var(--orange); border-radius: 2px; color: var(--white); font-family: "Noto Serif", serif; font-weight: 700; font-size: 15.5px; text-align: center; line-height: 42px; }

  .legal-links { position: absolute; left: 98px; top: 690px; font-size: 13.5px; color: var(--muted); }
  .legal-links .sep { margin: 0 18px; }
  .social { position: absolute; left: 995px; top: 686px; display: flex; gap: 7px; }
  .social span { width: 31px; height: 31px; border-radius: 50%; display: block; }
  .social .s1 { background: #4d6aa3; }
  .social .s2 { background: #e24a2b; }
  .social .s3 { background: #23b0ea; }

  .copyright-band { position: absolute; left: 0; top: 734px; width: 1200px; height: 81px; background: var(--band); text-align: center; line-height: 78px; font-size: 13.5px; color: var(--muted); }
</style>
</head>
<body>
  <header class="site-header">
    <div class="brand">JISTOTKA.CZ</div>
    <nav class="main-nav">
      <span class="nav-link">O NÁS</span>
      <span class="nav-link">CASTE DOTAZY</span>
      <span class="nav-link">KONTAKT</span>
      <span class="nav-button login">PRIHLASIT SE</span>
      <span class="nav-button register">REGISTROVAT</span>
    </nav>
  </header>

  <h1 class="intro-title">PROČ HLEDAT POJIŠTĚNÍ PŘES JISTOTKA.CZ?</h1>

  <svg class="product-carousel" width="410" height="124" viewBox="0 0 410 124">
    <polyline points="20,50 11,60 20,70" fill="none" stroke="var(--arrow)" stroke-width="2.5"/>
    <polyline points="390,50 399,60 390,70" fill="none" stroke="var(--arrow)" stroke-width="2.5"/>
    <circle cx="115" cy="60" r="43" fill="var(--white)" stroke="var(--blue)" stroke-width="1.5"/>
    <circle cx="295" cy="60" r="43" fill="var(--white)" stroke="var(--blue)" stroke-width="1.5"/>
    <circle cx="204" cy="60" r="58" fill="var(--blue)"/>
    <rect x="95" y="46" width="40" height="28" rx="4" fill="var(--blue)" role="img" aria-label="Ikona letadla – cestovní pojištění"/>
    <rect x="176" y="42" width="58" height="36" rx="6" fill="var(--white)" role="img" aria-label="Ikona převráceného auta – havarijní pojištění"/>
    <path d="M279 61 L295 46 L311 61 M284 57 V76 H292 V67 H298 V76 H306 V57" fill="none" stroke="var(--blue)" stroke-width="4" stroke-linejoin="round"/>
  </svg>
  <div class="product-label">HAVARIJNI POJISTENI</div>

  <form class="quote-form">
    <div class="field first-name">Jméno</div>
    <div class="field surname">Příjmení</div>
    <div class="field email">E-mail</div>
    <div class="consent"><span class="box"></span>Souhlasím s podmínkami použití</div>
    <div class="submit">SPOČÍTAT CENU</div>
  </form>

  <div class="legal-links">Terms of use<span class="sep">|</span>Privacy Policy.</div>
  <div class="social"><span class="s1"></span><span class="s2"></span><span class="s3"></span></div>

  <footer class="copyright-band">Copyright © 2017 - 2018 jistotka.cz</footer>
</body>
</html>
```